Tildens Biscuit Barn Website

I need a website for a diner/restaurant that has been established in a farming, oil and industrial community for over 15 years. The website needs to be simple in design, but that should demonstrate the mastery of skills of the designer. Our diner/restaurant is family oriented, patriotic but very rustic
Fb Address is fb.me/TildensBarn

Pictures of the restaurant

https://www.filecrate-example.net/s/qk72hdw01/Tildens_05.jpg

Pictures of About us

https://www.filecrate-example.net/sh/zm40vrt88/AboutUsPhotos

Article about Tilden's
https://www.filecrate-example.net/s/wp31nbx57/TildensBiscuitBarn1.PDF
https://www.filecrate-example.net/s/hy65lcu29/TildensBiscuitBarn2.PDF

Reason: I was slow to update with information.

Reason: I am just getting feedback to the designs posted. I wasn't sure of the limited feedback was limiting designers from submitting designs. That and running a business with 25 employees open 12 hours a day, being here 2 hours prior and 2-3 hours after makes for long days.

I've increased the first place prize and also added funds to the second and third place prizes for your effort.

I just need the files in PSD, not HTML 5 as originally requested. We can handle getting the coding part.

Ill have the contest finalized by Monday. Thanks for your patience.

Target Market(s)

Cross section of adults from 18-35 & 35-55.

Industry/Entity Type

Industrial

Font styles to use
Other font styles liked:
• ff tisa web pro or garamond premier pro

Requirements
Must have
• Must be clean, look nice and not look like an afterthought.
Nice to have
• Please see the last two documents for information about our restaurant, which was featured in our local newspaper.

```html
<!DOCTYPE html>
<html lang="en">
<head>
<meta charset="utf-8">
<title>Tilden's Biscuit Barn</title>
<link rel="stylesheet" href="https://fonts.googleapis.com/css2?family=Cabin+Sketch:wght@400;700&family=Kalam:wght@400;700&family=Passion+One:wght@400&family=Raleway:wght@400;600;700&display=swap">
<style>
:root{
  --wall:#f0efec;
  --wall-shade:#e2e1dd;
  --ink:#3f3f3f;
  --body-text:#6d6d6d;
  --heading:#5a5a5a;
  --ribbon:#2e2f2b;
  --ribbon-edge:#1c1d1a;
  --nav-text:#ffffff;
  --chalkboard:#1d1d1d;
  --chalk-area:#2a2a2a;
  --chalk:#efefef;
  --brand:#c6224c;
  --paper:#e9c27a;
  --paper-line:#b08a4e;
  --pin:#c8171f;
  --map:#d8d8d6;
  --frame:#8b7556;
  --bean:#4a2e20;
  --cup-rim:#e4e2de;
  --coffee:#2a1810;
  --footer-text:#444444;
}
*{box-sizing:border-box;margin:0;padding:0}
html,body{width:1200px;height:2556px;overflow:hidden}
body{position:relative;background:var(--wall);font-family:"Raleway",Arial,sans-serif;color:var(--ink)}

.site-header{position:absolute;left:0;top:0;width:1200px;height:837px;
  background:linear-gradient(180deg,#e8e7e3 0,var(--wall) 120px,var(--wall) 700px,#f6f5f3 837px)}
.brand{position:absolute;left:0;width:1200px;top:120px;text-align:center;
  font-family:"Raleway",Arial,sans-serif;font-weight:700;font-size:64px;color:var(--brand);letter-spacing:1px}
.coffee-beans{position:absolute;left:1068px;top:8px;width:124px;height:200px;
  background:linear-gradient(160deg,var(--bean) 0,#6b4631 100%);opacity:.85}

.main-nav{position:absolute;left:230px;top:298px;width:740px;height:50px}
.main-nav svg{position:absolute;left:0;top:0}
.main-nav ul{position:absolute;left:60px;top:0;width:620px;height:50px;list-style:none;display:flex;align-items:center;justify-content:space-between}
.main-nav li{color:var(--nav-text);font-size:16px;font-weight:600;letter-spacing:.5px;text-transform:uppercase}
.main-nav li.sep{color:#8a8a86;font-size:12px}

.welcome{position:absolute;left:144px;top:462px;width:595px}
.section-title{font-family:"Passion One",Impact,sans-serif;font-weight:400;color:var(--heading);
  font-size:48px;letter-spacing:2px;text-transform:uppercase;line-height:1}
.welcome p,.about p{font-size:12.5px;line-height:19px;color:var(--body-text);margin-top:14px}
.welcome .section-title{margin-bottom:22px}
.coffee-cup{position:absolute;left:806px;top:414px;width:394px;height:322px;
  background:linear-gradient(135deg,var(--cup-rim) 0,var(--cup-rim) 22%,var(--coffee) 45%,#3a2418 80%,var(--cup-rim) 100%)}

.menu{position:absolute;left:0;top:837px;width:1200px;height:713px;background:var(--chalkboard);
  font-family:"Cabin Sketch",cursive;color:var(--chalk)}
.menu-title{position:absolute;left:0;width:1200px;top:36px;text-align:center;font-size:58px;font-weight:700;letter-spacing:3px}
.menu-item{position:absolute;font-size:29px;letter-spacing:1px;text-transform:uppercase;font-weight:700;white-space:nowrap}
.menu-item .price{position:absolute;top:0;white-space:nowrap}
.col-left{left:147px}
.col-left .price{left:323px}
.col-right{left:648px}
.col-right .price{left:327px}
.cup-drawing{position:absolute;left:700px;top:423px;width:215px;height:232px;background:var(--chalk-area)}

.about{position:absolute;left:0;top:1550px;width:1200px;height:507px;
  background:linear-gradient(180deg,#e3e2de 0,var(--wall) 90px)}
.photo-frame{position:absolute;left:147px;top:93px;width:390px;height:331px;background:var(--frame);
  box-shadow:inset 0 0 0 4px #6e5b42,0 3px 6px rgba(0,0,0,.25);padding:36px 42px}
.photo-frame .photo{width:100%;height:100%;background:linear-gradient(180deg,#9c9c9c 0,#bdbdbd 45%,#6f6f6f 100%)}
.about-body{position:absolute;left:611px;top:100px;width:570px}
.about .section-title{margin-bottom:14px}

.location{position:absolute;left:0;top:2057px;width:1200px;height:387px}
.map{position:absolute;inset:0;background:linear-gradient(135deg,#cfcfcd 0,var(--map) 50%,#c4c4c2 100%)}
.note{position:absolute;left:718px;top:32px;width:334px;height:350px;background:var(--paper);
  box-shadow:0 2px 6px rgba(0,0,0,.3);padding:40px 22px 0 22px;font-family:"Kalam",cursive;color:#1d1d1d}
.note h3{font-size:24px;font-weight:400;line-height:30px;border-bottom:1px solid var(--paper-line)}
.note p{font-size:15.5px;line-height:30px;border-bottom:1px solid var(--paper-line)}
.note h3.hours{margin-top:16px}
.pin{position:absolute;left:700px;top:2px}

.site-footer{position:absolute;left:0;top:2444px;width:1200px;height:112px}
.copyright{position:absolute;left:147px;top:52px;font-size:12px;color:var(--footer-text)}
.social{position:absolute;left:850px;top:38px;display:flex;gap:18px;list-style:none}
.social li{width:40px;height:40px;border:2px solid #9a9a9a;border-radius:50%}
</style>
</head>
<body>

<header class="site-header">
  <div class="brand">Tilden's</div>
  <div class="coffee-beans" role="img" aria-label="Photo of roasted coffee beans scattered in the corner"></div>

  <nav class="main-nav">
    <svg width="740" height="50" viewBox="0 0 740 50" aria-hidden="true">
      <polygon points="0,10 40,10 40,44 0,44 14,27" fill="var(--ribbon-edge)"/>
      <polygon points="740,10 700,10 700,44 740,44 726,27" fill="var(--ribbon-edge)"/>
      <rect x="28" y="6" width="684" height="36" fill="var(--ribbon)"/>
      <line x1="52" y1="0" x2="52" y2="50" stroke="#111" stroke-width="2"/>
      <line x1="688" y1="0" x2="688" y2="50" stroke="#111" stroke-width="2"/>
    </svg>
    <ul>
      <li>Home</li><li class="sep">★</li>
      <li>About</li><li class="sep">★</li>
      <li>Menu</li><li class="sep">★</li>
      <li>History</li><li class="sep">★</li>
      <li>Contact</li>
    </ul>
  </nav>

  <section class="welcome">
    <h1 class="section-title">Welcome to our website</h1>
    <p>Every morning our ovens warm up before the sun, and the first pot of coffee is poured for the crews heading out to the fields, rigs and plants. We keep the recipes simple, the portions honest and the welcome the same for every family that walks through our door, whether it is their first visit or their five hundredth.</p>
    <p>Biscuits are rolled by hand, gravy is stirred low and slow, and the pie case is filled by noon. Pull up a chair, say hello to the regulars and stay as long as the coffee keeps coming.</p>
  </section>
  <div class="coffee-cup" role="img" aria-label="Photo of a white cup of black coffee seen from above"></div>
</header>

<section class="menu">
  <h2 class="menu-title">MENU</h2>

  <div class="menu-item col-left" style="top:152px">Cafe Latte<span class="price">$ 3.43</span></div>
  <div class="menu-item col-left" style="top:206px">Expresso<span class="price">$ 543</span></div>
  <div class="menu-item col-left" style="top:261px">Cafe Venillalatte<span class="price">$ 2.43</span></div>
  <div class="menu-item col-left" style="top:314px">Cafe Americano<span class="price">$ 7.43</span></div>
  <div class="menu-item col-left" style="top:368px">Cafe Latte<span class="price">$ 7.43</span></div>
  <div class="menu-item col-left" style="top:417px">Smoothie<span class="price">$ 7.43</span></div>
  <div class="menu-item col-left" style="top:472px">Cup of the Day<span class="price">$ 543</span></div>
  <div class="menu-item col-left" style="top:533px">Cafe Frappe<span class="price">$ 3.43</span></div>
  <div class="menu-item col-left" style="top:588px">Smoothie<span class="price">$ 7.43</span></div>

  <div class="menu-item col-right" style="top:152px">Cafe Frappe<span class="price">$ 3.43</span></div>
  <div class="menu-item col-right" style="top:206px">Cup of the Day<span class="price">$ 543</span></div>
  <div class="menu-item col-right" style="top:261px">Cold Brew<span class="price">$ 2.43</span></div>
  <div class="menu-item col-right" style="top:314px">Smoothie<span class="price">$ 7.43</span></div>
  <div class="menu-item col-right" style="top:368px">Iced Latte<span class="price">$ 7.43</span></div>

  <div class="cup-drawing" role="img" aria-label="Chalk illustration of a steaming coffee cup on a saucer"></div>
</section>

<section class="about">
  <div class="photo-frame">
    <div class="photo" role="img" aria-label="Black and white photo of the roadside diner with cars parked out front"></div>
  </div>
  <div class="about-body">
    <h2 class="section-title">About us</h2>
    <p>Tilden's opened its doors in a small roadside building more than fifteen years ago, serving breakfast to the farmers, oil workers and mill hands who keep this valley running. What started with six tables and one griddle has grown into a gathering place for the whole community. Many of our cooks and servers have been with us since the very first morning.</p>
    <p>We still fly the flag out front, still bake every biscuit from scratch and still know most of our guests by name. Our family is proud to share a table with yours, and we hope every plate feels a little like home.</p>
    <p>Stop by for a hot breakfast, a quick lunch or a slice of pie, and see why folks keep coming back.</p>
  </div>
</section>

<section class="location">
  <div class="map" role="img" aria-label="Street map showing the diner location"></div>
  <div class="note">
    <h3>Contact</h3>
    <p>4820 Millstone Hwy</p>
    <p>Harlow Springs, California</p>
    <h3 class="hours">Opening Times</h3>
    <p>Monday - Saturday: 9:00am - 9:00pm</p>
    <p>Sunday: 11:00am - 7:00pm</p>
    <p>Available by 7 days a week.</p>
  </div>
  <svg class="pin" width="60" height="70" viewBox="0 0 60 70" aria-hidden="true">
    <line x1="34" y1="30" x2="44" y2="58" stroke="#777" stroke-width="3"/>
    <circle cx="26" cy="22" r="16" fill="var(--pin)"/>
    <circle cx="21" cy="17" r="5" fill="#e9585e"/>
  </svg>
</section>

<footer class="site-footer">
  <p class="copyright">Copyright © 2013. All Rights Reserved.</p>
  <ul class="social">
    <li aria-label="Social link"></li>
    <li aria-label="Social link"></li>
    <li aria-label="Social link"></li>
    <li aria-label="Social link"></li>
  </ul>
</footer>

</body>
</html>
```